Postcard that needs a professional designer to create a great looking postcard

Direct mail postcard designed using the copy and graphics we have supplied. We need it to look professional, clean and eye catching.
We are marketing to builders who need to hire us to build the closets and storage in the homes they are contracted to build.

```html
<!DOCTYPE html>
<html lang="en">
<head>
<meta charset="utf-8">
<title>Harwell Closets – Builder Postcard</title>
<link rel="stylesheet" href="https://fonts.googleapis.com/css2?family=Source+Sans+3:ital,wght@0,400;0,600;1,400&display=swap">
<style>
  :root {
    --navy: #1f3566;
    --navy-text: #2b2f8f;
    --red: #e0322b;
    --ink: #2a2a2a;
    --rule: #c9c9c9;
    --paper: #ffffff;
    --backdrop: #d9d8d6;
    --wood-light: #d8c3a3;
    --closet-white: #e9e6e0;
  }
  * { margin: 0; padding: 0; box-sizing: border-box; }
  html, body { width: 921px; height: 1200px; overflow: hidden; }
  body {
    background: var(--backdrop);
    font-family: "Source Sans 3", Arial, sans-serif;
    color: var(--ink);
    position: relative;
  }
  .postcard {
    position: absolute;
    left: 150px;
    width: 659px;
    height: 510px;
    background: var(--paper);
    box-shadow: 0 3px 10px rgba(0,0,0,.25);
    overflow: hidden;
  }
  .postcard--front { top: 74px; }
  .postcard--back { top: 611px; }

  .photo { position: absolute; }
  .front-hero { left: 0; top: 0; width: 355px; height: 347px;
    background: linear-gradient(120deg, #e3d7c6 0%, #d8c3a3 45%, #a9b3c2 100%); }
  .front-thumbs { position: absolute; left: 0; top: 347px; width: 355px; height: 103px; display: flex; gap: 3px; background: var(--paper); }
  .front-thumbs .thumb { flex: 1; height: 100%; }
  .thumb--office { background: linear-gradient(160deg, #6d4a32, #c9b8a3); }
  .thumb--pantry { background: linear-gradient(160deg, #e8eef2, #9db2c4); }
  .thumb--shelves { background: linear-gradient(160deg, #efece6, #b9b1a6); }

  .brand {
    text-align: center;
    color: var(--navy);
    font-weight: 600;
    line-height: 1.1;
  }
  .brand__dot { display: inline-block; width: 14px; height: 14px; border-radius: 50%; background: var(--red); margin-bottom: 8px; }
  .brand__name { font-size: 24px; display: block; }
  .brand__sub { font-size: 17px; display: block; }

  .front-panel { position: absolute; left: 355px; top: 0; width: 304px; height: 450px; }
  .front-panel .brand { position: absolute; left: 0; right: 0; top: 24px; }
  .rule { position: absolute; left: 16px; right: 16px; height: 2px; background: var(--rule); }
  .rule--top { top: 127px; }
  .rule--bottom { top: 244px; }
  .headline {
    position: absolute; left: 20px; right: 14px; top: 142px;
    color: var(--red); font-size: 15.5px; line-height: 22px; text-transform: uppercase;
  }
  .benefits { position: absolute; left: 20px; right: 12px; top: 262px; list-style: none; font-size: 12.5px; line-height: 17px; }
  .benefits li { position: relative; padding-left: 18px; margin-bottom: 6px; }
  .benefits li svg { position: absolute; left: 0; top: 3px; }
  .cta { position: absolute; left: 0; right: 0; text-align: center; color: var(--navy-text); font-size: 14px; line-height: 17px; }
  .front-panel .cta { top: 404px; }

  .tagline-band {
    position: absolute; left: 0; top: 450px; width: 659px; height: 60px;
    background: var(--navy); color: #fff; font-size: 16px; letter-spacing: .2px;
    display: flex; align-items: center; justify-content: center; text-transform: uppercase;
  }

  .back-message { position: absolute; left: 0; top: 0; width: 334px; height: 510px; }
  .back-message .brand { position: absolute; left: 0; right: 0; top: 22px; }
  .back-closet { left: 0; top: 132px; width: 334px; height: 159px;
    background: linear-gradient(180deg, #efece6 0%, var(--closet-white) 60%, #cfc8bd 100%); }
  .letter { position: absolute; left: 16px; right: 16px; top: 297px; text-align: center; font-size: 13.5px; line-height: 16.5px; }
  .letter p + p { margin-top: 16px; }
  .signature { margin-top: 8px; font-style: italic; font-size: 14px; }
  .back-footer { position: absolute; left: 0; top: 452px; width: 334px; height: 58px; background: var(--navy); }
  .back-footer .cta { top: 11px; color: #fff; }

  .indicia {
    position: absolute; left: 553px; top: 24px; width: 73px; height: 77px;
    border: 1px solid #9a9a9a; text-align: center; font-size: 10px; line-height: 13px; padding-top: 7px;
  }
  .indicia b { font-weight: 600; }
  .address-line { position: absolute; left: 393px; width: 233px; height: 1px; background: var(--rule); }
</style>
</head>
<body>

<section class="postcard postcard--front">
  <div class="photo front-hero" role="img" aria-label="Smiling woman standing beside a wooden closet with folded clothes"></div>
  <div class="front-thumbs">
    <div class="thumb thumb--office" role="img" aria-label="Built-in home office desk"></div>
    <div class="thumb thumb--pantry" role="img" aria-label="White pantry shelving"></div>
    <div class="thumb thumb--shelves" role="img" aria-label="Open shelves with storage baskets"></div>
  </div>

  <div class="front-panel">
    <div class="brand">
      <span class="brand__dot"></span>
      <span class="brand__name">Harwell Closets</span>
      <span class="brand__sub">and Storage Systems</span>
    </div>
    <div class="rule rule--top"></div>
    <p class="headline">It's frustrating and time consuming trying to decide how to provide quality custom closets for your homeowner.</p>
    <div class="rule rule--bottom"></div>
    <ul class="benefits">
      <li><svg width="10" height="10" viewBox="0 0 10 10"><circle cx="5" cy="5" r="5" fill="#2b2f8f"/><path d="M4 3l2 2-2 2" stroke="#fff" stroke-width="1.3" fill="none"/></svg>You must have the same high quality in the closets that you provide in the rest of the home</li>
      <li><svg width="10" height="10" viewBox="0 0 10 10"><circle cx="5" cy="5" r="5" fill="#2b2f8f"/><path d="M4 3l2 2-2 2" stroke="#fff" stroke-width="1.3" fill="none"/></svg>You need someone that will be on time and stay within the budget</li>
      <li><svg width="10" height="10" viewBox="0 0 10 10"><circle cx="5" cy="5" r="5" fill="#2b2f8f"/><path d="M4 3l2 2-2 2" stroke="#fff" stroke-width="1.3" fill="none"/></svg>Have design options, color choices, and detailed plans to re-view with the homeowner</li>
    </ul>
    <p class="cta">Get a free design estimate<br>www.harwellclosetsandstoragesystems.com</p>
  </div>

  <div class="tagline-band">Custom boilt closets and storege system so have place for everything</div>
</section>

<section class="postcard postcard--back">
  <div class="back-message">
    <div class="brand">
      <span class="brand__dot"></span>
      <span class="brand__name">Harwell Closets</span>
      <span class="brand__sub">and Storage Systems</span>
    </div>
    <div class="photo back-closet" role="img" aria-label="White custom walk-in closet with hanging clothes, drawers and shoe shelves"></div>
    <div class="letter">
      <p>There are many contractors that are called heroes by the homeowner because of the closets Harwell Closets has provided.</p>
      <p>Naturally, you will want to call Harwell Closets to relieve your stress and frustration about having great custom closets and not just painted particle board.</p>
      <p class="signature">Daniel and Marcus Harwell</p>
    </div>
    <div class="back-footer">
      <p class="cta">Get a free design estimate<br>www.harwellclosetsandstoragesystems.com</p>
    </div>
  </div>

  <div class="indicia">PRSRT STD<br>ECRWSS<br>U.S. POSTAGE<br><b>PAID</b><br>EDDM RETAIL</div>
  <div class="address-line" style="top:211px"></div>
  <div class="address-line" style="top:249px"></div>
  <div class="address-line" style="top:287px"></div>
</section>

</body>
</html>
```